New Business Card Design for Engineering and Surveying Company

We need a new design template for our business cards. We are a civil engineering, land surveying and pipeline integrity business. Please see dkhpartners.com for details. We need a bold, new business card design to complement our rebranding and marketing program. We have anew logo and attached vectro file. Please find additional details below. I am available to answer any questions.

Target Market(s)

Contractors, business owners, oil companies

Contact Information for Business Card

Needs to be customizable for different people (name, title, cell)

Font styles to use
Sans Serif
Other font styles liked:
• See eps file

Requirements
Must have
• Example Information:
Trevor Ashcombe

T:409-555-0173
M: 202-555-0148
tashcombe@dkhprtnrs.com

Address: 1875 Pinecrest Parkway, Beaumont, Texas 77703
Email: tolvanrey@dkhpartners.com
Website: www.dkhpartners.com
Nice to have
• I would like the back of the card to have the logo on a bold background with the text below:

[logo]
DORAN KESSLING & PARTNERS
CIVIL ENGINEERING | LAND SURVEYING | PIPELINE INTEGRITY

The reverse side should have the contact information for the person (example above), a smaller version of the logo and a graphic

```html
<!DOCTYPE html>
<html lang="en">
<head>
<meta charset="utf-8">
<title>DKP Business Card</title>
<link href="https://fonts.googleapis.com/css2?family=Mulish:wght@400;500;800&display=swap" rel="stylesheet">
<style>
  :root {
    --backdrop: #949494;
    --card: #000000;
    --ink: #ffffff;
    --accent: #e51d2e;
  }
  * { box-sizing: border-box; margin: 0; padding: 0; }
  html, body { width: 1200px; height: 960px; overflow: hidden; }
  body {
    background: var(--backdrop);
    font-family: "Mulish", "Helvetica Neue", Arial, sans-serif;
    color: var(--ink);
    position: relative;
  }
  .card {
    position: absolute;
    left: 245px;
    width: 710px;
    height: 404px;
    background: var(--card);
    border-radius: 28px;
  }
  .card--front { top: 56px; }
  .card--back { top: 500px; }

  .holder { position: absolute; left: 65px; top: 66px; }
  .holder__name { color: var(--accent); font-size: 25px; font-weight: 500; line-height: 1.2; }
  .holder__title { font-size: 19px; font-weight: 400; margin-top: 2px; }

  .contact-list { position: absolute; list-style: none; font-size: 17px; line-height: 24px; }
  .contact-list li { display: flex; align-items: center; gap: 8px; white-space: nowrap; }
  .contact-list svg { width: 15px; height: 15px; flex: none; }
  .contact-list--personal { left: 65px; top: 278px; }
  .contact-list--company { left: 426px; top: 303px; }

  .brand-mark {
    position: absolute;
    display: flex;
    align-items: center;
    gap: 12px;
    font-weight: 800;
    color: var(--ink);
    line-height: 1;
    letter-spacing: 2px;
  }
  .brand-mark__square { background: var(--accent); flex: none; }
  .card--front .brand-mark { left: 426px; top: 172px; font-size: 60px; }
  .card--front .brand-mark__square { width: 22px; height: 22px; }

  .address { position: absolute; left: 426px; top: 238px; font-size: 17px; line-height: 24px; }

  .card--back .brand-mark { left: 50%; top: 138px; transform: translateX(-50%); font-size: 88px; gap: 18px; }
  .card--back .brand-mark__square { width: 30px; height: 30px; }
  .company-name {
    position: absolute; top: 296px; width: 100%; text-align: center;
    color: var(--accent); font-size: 18px; font-weight: 400;
  }
  .services {
    position: absolute; top: 324px; width: 100%; text-align: center;
    font-size: 18px; font-weight: 400;
  }
</style>
</head>
<body>
  <section class="card card--front">
    <div class="holder">
      <div class="holder__name">Trevor Ashcombe</div>
      <div class="holder__title">Manager</div>
    </div>

    <ul class="contact-list contact-list--personal">
      <li>
        <svg viewBox="0 0 16 16"><path d="M4 2c-2 1-2.5 3-1 6s4 6 7 6.5c1.5.3 2.5-.5 3-1.5l-2.5-2-1.5 1c-1.5-.5-3.5-2.5-4-4l1-1.5z" fill="var(--accent)"/></svg>
        409-555-0173
      </li>
      <li>
        <svg viewBox="0 0 16 16"><rect x="4" y="1" width="8" height="14" rx="1.5" fill="none" stroke="var(--accent)" stroke-width="1.6"/><rect x="7" y="12" width="2" height="1.2" fill="var(--accent)"/></svg>
        202-555-0148
      </li>
      <li>
        <svg viewBox="0 0 16 16"><rect x="1" y="4" width="14" height="9" fill="var(--accent)"/><path d="M1 4l7 5 7-5" fill="none" stroke="#000" stroke-width="1.2"/></svg>
        tashcombe@dkhprtnrs.com
      </li>
    </ul>

    <div class="brand-mark">
      <span class="brand-mark__square"></span>
      <span class="brand-mark__name">DKP</span>
    </div>

    <address class="address" style="font-style:normal">
      1875 Pinecrest Parkway<br>
      Beaumont, Texas 77703
    </address>

    <ul class="contact-list contact-list--company">
      <li>
        <svg viewBox="0 0 16 16"><rect x="1" y="4" width="14" height="9" fill="var(--accent)"/><path d="M1 4l7 5 7-5" fill="none" stroke="#000" stroke-width="1.2"/></svg>
        tolvanrey@dkhpartners.com
      </li>
      <li>
        <svg viewBox="0 0 16 16" fill="none" stroke="var(--accent)" stroke-width="1.3"><circle cx="8" cy="8" r="6.3"/><ellipse cx="8" cy="8" rx="2.8" ry="6.3"/><path d="M1.7 8h12.6M3 4.5h10M3 11.5h10"/></svg>
        www.dkhpartners.com
      </li>
    </ul>
  </section>

  <section class="card card--back">
    <div class="brand-mark">
      <span class="brand-mark__square"></span>
      <span class="brand-mark__name">DKP</span>
    </div>
    <div class="company-name">DORAN KESSLING &amp; PARTNERS</div>
    <div class="services">CIVIL ENGINEERING | LAND SURVEYING | PIPELINE INTEGRITY</div>
  </section>
</body>
</html>
```